Bright and beautiful business card for a coach

I'm a personal and business coach based in Perth, Australia. I need a business card that whilst subtle and elegant, will stand out and appeal on a table full of cards.

My business name is Tide Mentoring and the business card must represent the warmth and brightness implied in the name, without being gimmicky. It must have a warmth and appeal and be easy to read.

I prefer clean, minimalist designs.

It must align with the feel of my website and socials: https://www.tidementoring.com.au/
https://www.instagram.com/tidementoringau/
https://www.facebook.com/tidementoringau
Updates

Hi Designers Thank you so much for taking the time to submit designs. I wonder if I could have explained myself a little better. Most of the designs that have been submitted look rather formal and many have quite corporate looking embellishments on them (to my eye). I would like softer, warmer, more organic. I’m open to people playing about and being more abstract, using softer embellishments (e.g the line drawing flowers and grasses I’ve used in my socials) incorporating other colours from my palette or like the social icons in my email signature (in PDF), perhaps playing with size/oversize, playing with the bleed. Please don’t be constrained by what I’ve already done, it merely needs to compliment. I’m sorry if I’m not using the right words or have led you astray. I’m no designer, but I’ve done my website, socials, email signature etc all myself (my logo was a design contest) and I was really hoping for my business card to be something more creative than I could have made with a template. Reminder: No black cards/sides please. Thank you 😊

Target Market(s)

Individuals, most likely but not all female. Creative thinkers. Likely professionals.

Industry/Entity Type

Business & Personal Coach

Contact Information for Business Card

(Tide Mentoring Logo) Name: Maren Delsby; Title: Business & Personal Coach; Phone number: +61 (0)438 915307; Email: maren@tidementoring.com.au; Website: https://tidementoring.com.au; Social icons for Facebook, Instagram & LinkedIn: @tidementoringAU. Optional strapline: "A thinking partner to help you cut through the noise"

Font styles to use
Sans Serif

Colors
00AB8E
00BBA5
67D7C9
C6EFE9
E9F9F6
59FF00
82FF00
B8FF75
E3FFCB
F4FFEA
FFC000
F8CF3A
FAE287
FDF2CF
FEFAEE

Requirements
Must have
• Must align with feel of my website and socials. Must have a pop of #FFC000 (possibly whole of one side, or at least a block). Bright or white background. Easy to read.
Nice to have
• Possibly incorporate the sunshine/grass picture I have used in website and socials - will upload.
Should not have
• Must not be black or dark. Not impersonal or corporate looking.

```html
<!DOCTYPE html>
<html lang="en">
<head>
<meta charset="utf-8">
<title>Tide Mentoring – Business Card</title>
<link rel="stylesheet" href="https://fonts.googleapis.com/css2?family=Lato:wght@400;700&display=swap">
<style>
  :root {
    --backdrop: #bfbfbf;
    --sun: #fcc10f;
    --sun-soft: #fdd04a;
    --paper: #ffffff;
    --sprig-grey: #ececec;
    --ink-white: #ffffff;
    --social-dot: rgba(255, 255, 255, 0.85);
  }
  * { box-sizing: border-box; margin: 0; padding: 0; }
  html, body { width: 1200px; height: 1000px; overflow: hidden; }
  body {
    background: var(--backdrop);
    font-family: "Lato", Arial, sans-serif;
    position: relative;
  }
  .card {
    position: absolute;
    top: 347px;
    width: 489px;
    height: 279px;
    overflow: hidden;
    box-shadow: 0 6px 14px rgba(0, 0, 0, 0.18);
  }
  .card--front { left: 75px; background: var(--paper); }
  .card--back { left: 628px; background: var(--sun); }

  .sprig { position: absolute; }
  .card--front .sprig { background: var(--sprig-grey); }
  .card--back .sprig { background: var(--sun-soft); }
  .sprig--top-left { left: 0; top: 0; width: 84px; height: 182px; border-radius: 0 0 50px 0; }
  .sprig--bottom-right { right: 0; bottom: 0; width: 172px; height: 80px; border-radius: 60px 0 0 0; }

  .brand-disc {
    position: absolute;
    border-radius: 50%;
    display: flex;
    align-items: center;
    justify-content: center;
    text-align: center;
    font-weight: 700;
    letter-spacing: 0.12em;
    text-transform: uppercase;
  }
  .card--front .brand-disc {
    left: 167px; top: 61px; width: 154px; height: 154px;
    background: var(--sun); color: var(--ink-white); font-size: 13px;
  }
  .card--back .brand-disc {
    left: 324px; top: 31px; width: 133px; height: 133px;
    background: var(--paper); color: var(--sun); font-size: 11px;
  }

  .profile {
    position: absolute;
    left: 98px;
    top: 56px;
    color: var(--ink-white);
  }
  .profile__name { font-size: 30px; font-weight: 700; line-height: 1.05; }
  .profile__title { font-size: 14px; font-weight: 700; margin-top: 1px; }
  .contact { list-style: none; margin-top: 24px; font-size: 15px; line-height: 19px; }

  .social {
    position: absolute;
    left: 96px;
    top: 220px;
    display: flex;
    align-items: center;
    gap: 6px;
    color: var(--ink-white);
    font-size: 11px;
    font-weight: 700;
  }
  .social__dot { width: 22px; height: 22px; border-radius: 50%; background: var(--social-dot); }
  .social__handle { margin-left: 2px; }
</style>
</head>
<body>
  <section class="card card--front" aria-label="Card front">
    <div class="sprig sprig--top-left" role="img" aria-label="Line drawing of leaves and tulip buds"></div>
    <div class="brand-disc">Tide<br>Mentoring</div>
    <div class="sprig sprig--bottom-right" role="img" aria-label="Line drawing of tulips and grasses"></div>
  </section>

  <section class="card card--back" aria-label="Card back">
    <div class="sprig sprig--top-left" role="img" aria-label="White line drawing of leaves and tulip buds"></div>
    <div class="profile">
      <h1 class="profile__name">Maren Delsby</h1>
      <p class="profile__title">Business &amp; Personal Coach</p>
      <ul class="contact">
        <li>maren@tidementoring.com.au</li>
        <li>tidementoring.com.au</li>
        <li>+61 (0)438 915307</li>
      </ul>
    </div>
    <div class="social">
      <span class="social__dot"></span>
      <span class="social__dot"></span>
      <span class="social__dot"></span>
      <span class="social__handle">@tidementoringAU</span>
    </div>
    <div class="brand-disc">Tide<br>Mentoring</div>
    <div class="sprig sprig--bottom-right" role="img" aria-label="White line drawing of tulips and grasses"></div>
  </section>
</body>
</html>
```